Poster for pawn shop lobby

Looking for green and gold as my colors, like the picture shown of my old poster. This time I'm contemplating with doing pictures as well as just text. Here are ideas of things I buy and give loans on. We want to emphasize jewelry, laptops, game systems, tools. I'm open-minded.
Old & Broken Gold
Jewelry & Collectibles
Diamonds
Video Games & Systems
Up-to-date Computers & Laptops
Tablets
Cameras
Power Tools
Home & Garden Equipment
Sports Equipment
Watches
Antique Collectibles
Musical Instruments
And anything else of value
Shop

```html
<!DOCTYPE html>
<html lang="en">
<head>
<meta charset="utf-8">
<title>We'll Loan or Pay You Cash On</title>
<link href="https://fonts.googleapis.com/css2?family=Anton&family=Arimo:wght@700&display=swap" rel="stylesheet">
<style>
  :root {
    --green-deep: #0b6b2c;
    --green-mid: #17903e;
    --green-light: #3fb54a;
    --gold-bright: #ffe21a;
    --gold-mid: #f3c300;
    --gold-deep: #c98f00;
    --gold-text: #ffd633;
    --title-green: #3fb83a;
    --title-red: #d7141c;
    --ink: #111;
    --white: #ffffff;
  }
  * { margin: 0; padding: 0; box-sizing: border-box; }
  html, body { width: 848px; height: 1200px; overflow: hidden; background: var(--green-mid); }
  .poster {
    position: relative;
    width: 848px;
    height: 1200px;
    overflow: hidden;
    background: linear-gradient(180deg, var(--green-deep) 0%, var(--green-mid) 35%, #1d9a40 70%, var(--green-light) 100%);
  }
  .money-backdrop {
    position: absolute;
    left: 0; right: 0; bottom: 0;
    height: 560px;
    background:
      radial-gradient(ellipse 220px 330px at 745px 300px, rgba(240,190,40,0.5), rgba(240,190,40,0) 75%),
      linear-gradient(170deg, rgba(120,200,90,0) 0%, rgba(150,215,110,0.4) 60%, rgba(170,225,120,0.55) 100%);
  }
  .header { position: absolute; top: 0; left: 0; width: 848px; height: 260px; }
  .title-text {
    font-family: "Anton", "Impact", sans-serif;
    text-anchor: middle;
    paint-order: stroke fill;
    stroke-linejoin: round;
  }
  .offer-list {
    position: absolute;
    top: 266px;
    left: 0;
    width: 848px;
    list-style: none;
  }
  .offer-item {
    height: 52px;
    display: flex;
    align-items: center;
    justify-content: center;
    gap: 14px;
    font-family: "Arimo", Arial, sans-serif;
    font-weight: 700;
    font-size: 35px;
    line-height: 1;
    color: var(--white);
    white-space: nowrap;
    background: linear-gradient(90deg, rgba(255,255,255,0) 0%, rgba(255,255,255,0.07) 20%, rgba(255,255,255,0.07) 80%, rgba(255,255,255,0) 100%);
    border-bottom: 2px solid rgba(255,255,255,0.05);
  }
  .offer-item--featured {
    color: var(--gold-text);
    font-size: 37px;
    text-shadow: 0 2px 0 rgba(0,60,20,0.55);
  }
  .coin { width: 26px; height: 26px; flex: none; }
  .feature-gallery {
    position: absolute;
    left: 28px;
    top: 1010px;
    width: 792px;
    height: 170px;
    display: grid;
    grid-template-columns: repeat(4, 1fr);
    gap: 16px;
  }
  .feature-photo {
    border-radius: 14px;
    border: 4px solid var(--gold-mid);
    box-shadow: 0 4px 10px rgba(0,50,15,0.45);
  }
  .feature-photo--jewelry { background: radial-gradient(circle at 45% 40%, #fff3b0, #e6b422 55%, #9a6d08); }
  .feature-photo--laptops { background: linear-gradient(160deg, #d9dee3, #8d959c 60%, #4a5157); }
  .feature-photo--games { background: linear-gradient(160deg, #5a5f6a, #2c2f36 60%, #15171b); }
  .feature-photo--tools { background: linear-gradient(160deg, #f0c640, #d88a12 55%, #3b3b3b); }
</style>
</head>
<body>
<div class="poster">
  <div class="money-backdrop" role="img" aria-label="Banknotes spread across the lower poster with a large gold dollar sign on the right"></div>

  <svg class="header" viewBox="0 0 848 260" aria-label="We'll loan or pay you cash on">
    <defs>
      <linearGradient id="goldFill" x1="0" y1="0" x2="0" y2="1">
        <stop offset="0" stop-color="var(--gold-bright)"/>
        <stop offset="0.6" stop-color="var(--gold-mid)"/>
        <stop offset="1" stop-color="var(--gold-deep)"/>
      </linearGradient>
    </defs>
    <path d="M0 0 H848 V130 Q424 360 0 136 Z" fill="url(#goldFill)"/>
    <path d="M0 0 H300 V60 Q160 130 0 120 Z" fill="rgba(255,240,140,0.35)" role="img" aria-label="Stacked gold bars"/>
    <path d="M0 136 Q424 360 848 130" fill="none" stroke="var(--green-deep)" stroke-width="10"/>
    <g class="title-text">
      <text x="428" y="102" font-size="64" stroke="var(--white)" stroke-width="14" fill="var(--white)">WE'LL <tspan font-size="76">LOAN</tspan> OR</text>
      <text x="428" y="102" font-size="64" stroke="var(--ink)" stroke-width="6" fill="var(--title-green)">WE'LL <tspan font-size="76" fill="var(--title-red)">LOAN</tspan> OR</text>
      <text x="428" y="188" font-size="64" stroke="var(--white)" stroke-width="14" fill="var(--white)">PAY YOU <tspan font-size="76">CASH</tspan> ON</text>
      <text x="428" y="188" font-size="64" stroke="var(--ink)" stroke-width="6" fill="var(--title-green)">PAY YOU <tspan font-size="76" fill="var(--title-red)">CASH</tspan> ON</text>
    </g>
  </svg>

  <svg width="0" height="0" style="position:absolute">
    <symbol id="coin" viewBox="0 0 26 26">
      <circle cx="13" cy="13" r="12" fill="#f6b800" stroke="#7a4b00" stroke-width="1.5"/>
      <circle cx="13" cy="13" r="8.5" fill="#ffd84a"/>
      <text x="13" y="18" font-family="Arimo, Arial, sans-serif" font-weight="700" font-size="13" text-anchor="middle" fill="#8a5a00">$</text>
    </symbol>
  </svg>

  <ul class="offer-list">
    <li class="offer-item"><svg class="coin"><use href="#coin"/></svg>Old &amp; Broken Gold<svg class="coin"><use href="#coin"/></svg></li>
    <li class="offer-item offer-item--featured"><svg class="coin"><use href="#coin"/></svg>Jewelry &amp; Collectibles<svg class="coin"><use href="#coin"/></svg></li>
    <li class="offer-item"><svg class="coin"><use href="#coin"/></svg>Diamonds<svg class="coin"><use href="#coin"/></svg></li>
    <li class="offer-item offer-item--featured"><svg class="coin"><use href="#coin"/></svg>Video Games &amp; Systems<svg class="coin"><use href="#coin"/></svg></li>
    <li class="offer-item offer-item--featured"><svg class="coin"><use href="#coin"/></svg>Up-to-date Computers &amp; Laptops<svg class="coin"><use href="#coin"/></svg></li>
    <li class="offer-item"><svg class="coin"><use href="#coin"/></svg>Tablets<svg class="coin"><use href="#coin"/></svg></li>
    <li class="offer-item"><svg class="coin"><use href="#coin"/></svg>Cameras<svg class="coin"><use href="#coin"/></svg></li>
    <li class="offer-item offer-item--featured"><svg class="coin"><use href="#coin"/></svg>Power Tools<svg class="coin"><use href="#coin"/></svg></li>
    <li class="offer-item"><svg class="coin"><use href="#coin"/></svg>Home &amp; Garden Equipment<svg class="coin"><use href="#coin"/></svg></li>
    <li class="offer-item"><svg class="coin"><use href="#coin"/></svg>Sports Equipment<svg class="coin"><use href="#coin"/></svg></li>
    <li class="offer-item"><svg class="coin"><use href="#coin"/></svg>Watches<svg class="coin"><use href="#coin"/></svg></li>
    <li class="offer-item"><svg class="coin"><use href="#coin"/></svg>Antique Collectibles<svg class="coin"><use href="#coin"/></svg></li>
    <li class="offer-item"><svg class="coin"><use href="#coin"/></svg>Musical Instruments<svg class="coin"><use href="#coin"/></svg></li>
    <li class="offer-item"><svg class="coin"><use href="#coin"/></svg>And anything else of value<svg class="coin"><use href="#coin"/></svg></li>
  </ul>

  <div class="feature-gallery">
    <div class="feature-photo feature-photo--jewelry" role="img" aria-label="Photo of gold rings, chains and diamond jewelry"></div>
    <div class="feature-photo feature-photo--laptops" role="img" aria-label="Photo of an open laptop computer"></div>
    <div class="feature-photo feature-photo--games" role="img" aria-label="Photo of a video game console with controllers"></div>
    <div class="feature-photo feature-photo--tools" role="img" aria-label="Photo of a cordless drill and power tools"></div>
  </div>
</div>
</body>
</html>
```